Business card design needed

A Moth's Fern

I would like a design for a small business specializing in earrings made from Tasmanian timber combined with coloured beads. I see the brand as a modern take on wooden earrings, fun and beautiful with the wood being laser cut Tasmanian timber combined with a coloured sometimes metallic bead.

I see the logo design as a little cute, perhaps a ladybug on a leaf and would like a combination of green and white. I have seen a quirky take on the traditional red ladybug done in pink with black spots on a green leaf that I like but I'm very open to ideas and suggestions.

Target Market(s)

Women primarily aged 20-50

Industry/Entity Type

Small Business

Contact Information for Business Card

A Moth's Fern
Tasmanian Timber & Beaded Design Earrings

www.pagebook.example/amothsfern
www.craftnook.example/amothsfern

Logo Text

A Moth's Fern

Requirements
Must have
• Must have some white on the business card. The cards are being matched with Tasmanian Timber earrings so whites and greens with a splash of colour is okay, but nothing to crazy or bright.

```html
<!DOCTYPE html>
<html lang="en">
<head>
<meta charset="utf-8">
<title>A Moth's Fern – Business Card</title>
<link rel="stylesheet" href="https://fonts.googleapis.com/css2?family=Source+Sans+3:wght@400&display=swap">
<style>
  :root {
    --card-bg: #ffffff;
    --ink: #000000;
    --leaf-green: #33ff00;
    --rule-red: #ee1c1c;
    --text-font: "Source Sans 3", "Myriad Pro", Arial, sans-serif;
  }
  html, body {
    margin: 0;
    padding: 0;
    overflow: hidden;
    background: var(--card-bg);
  }
  .card {
    position: relative;
    width: 1200px;
    height: 693px;
    background: var(--card-bg);
    font-family: var(--text-font);
    color: var(--ink);
    overflow: hidden;
  }
  .brand {
    position: absolute;
    left: 0;
    top: 150px;
    width: 1200px;
    height: 100px;
    display: flex;
    align-items: center;
    justify-content: center;
    gap: 26px;
    padding-left: 44px;
    box-sizing: border-box;
  }
  .brand-dot {
    flex: none;
    width: 90px;
    height: 90px;
    border-radius: 50%;
    background: var(--leaf-green);
  }
  .brand-name {
    margin: 0;
    font-size: 84px;
    font-weight: 400;
    line-height: 1;
    white-space: nowrap;
  }
  .tagline {
    position: absolute;
    left: 265px;
    top: 284px;
    width: 754px;
    margin: 0;
    text-align: center;
    font-size: 24px;
    line-height: 1;
    letter-spacing: 0.1em;
    white-space: nowrap;
  }
  .divider {
    position: absolute;
    left: 265px;
    top: 343px;
    width: 754px;
    height: 0;
    border-top: 3px solid var(--rule-red);
  }
  .person {
    position: absolute;
    left: 312px;
    top: 367px;
    width: 600px;
    margin: 0;
    text-align: center;
    font-size: 25px;
    line-height: 34.3px;
  }
  .contact {
    position: absolute;
    left: 312px;
    top: 529px;
    width: 600px;
    margin: 0;
    text-align: center;
    font-size: 20px;
    line-height: 27.5px;
  }
  .person span, .contact span { display: block; }
</style>
</head>
<body>
  <div class="card">
    <div class="brand">
      <div class="brand-dot"></div>
      <h1 class="brand-name">A Moth's Fern</h1>
    </div>
    <p class="tagline">Tasmanian Timber &amp; Beaded Design Earrings</p>
    <div class="divider"></div>
    <p class="person">
      <span class="person-name">Your Name goes here</span>
      <span class="person-title">(Chief Executive Officer, CEO, or President)</span>
      <span class="person-address">233 Adress here, Adress</span>
      <span class="person-address">Adress here</span>
    </p>
    <p class="contact">
      <span class="contact-phone">P: (555)010-1212 F: (555)010-1213</span>
      <span class="contact-email">hello@amothsfern.example</span>
      <span class="contact-web">www.pagebook.example/amothsfern</span>
      <span class="contact-web">www.craftnook.example/amothsfern</span>
    </p>
  </div>
</body>
</html>
```